HR services to some of biggest Silicon Valley Tech companies needs a new website

We need a new website design probably 4-5 pages initially. Here are some websites we like the look of https://quintarimhub.com/ , https://www.mervoly.com/ and https://tavrine.com/ .
Updates

Slow in providing feedback

Target Market(s)

Silicon valley tech companies

Industry/Entity Type

HR

Coding

Coded - Design and coding required

Number of Pages Required

5+ page

Requirements
Nice to have
• any stock photos or images should show a diverse group of people. Our client base is very diverse

```html
<!DOCTYPE html>
<html lang="en">
<head>
<meta charset="utf-8">
<title>Summit HR Consulting</title>
<link href="https://fonts.googleapis.com/css2?family=Poppins:wght@400;500;600;700&family=Rubik:wght@500&display=swap" rel="stylesheet">
<style>
:root{
  --yellow:#fcc526;
  --yellow-soft:#fdf1c6;
  --dark:#333333;
  --darker:#222222;
  --gray:#5d5d5d;
  --text:#555555;
  --light:#f1f1f1;
  --white:#ffffff;
}
*{margin:0;padding:0;box-sizing:border-box}
html,body{width:1200px;height:3566px;overflow:hidden}
body{position:relative;font-family:'Poppins',sans-serif;color:var(--text);background:var(--white)}
.abs{position:absolute}
h1,h2,h3{font-family:'Rubik',sans-serif;font-weight:500;color:#222}

/* header */
.brand{left:60px;top:48px;font-weight:600;font-size:20px;color:var(--gray);letter-spacing:1px;line-height:22px}
.brand small{display:block;font-size:10px;letter-spacing:3px;font-weight:500}
.brand-mark{left:84px;top:14px;width:30px;height:30px;border-radius:50%;background:var(--yellow)}
.header-line{left:0;top:97px;width:320px;height:3px;background:var(--yellow)}
.info{font-size:11px;line-height:16px;color:var(--text)}
.info b{display:block;font-weight:600;font-size:10px;color:#333}
.info-icon{width:30px;height:30px}
.quote-btn{left:975px;top:18px;width:135px;height:38px;background:var(--gray);color:#fff;font-size:14px;font-weight:500;display:flex;align-items:center;justify-content:center;clip-path:polygon(0 0,100% 0,100% 70%,88% 100%,0 100%)}
.navbar{left:300px;top:75px;width:900px;height:37px;background:var(--yellow);clip-path:polygon(30px 0,100% 0,100% 100%,0 100%)}
.nav{left:388px;top:75px;height:37px;display:flex;align-items:center;gap:32px;font-size:12px;font-weight:500;color:#fff}
.nav .active{color:#222}

/* hero */
.hero{left:0;top:112px;width:1200px;height:660px;background:linear-gradient(100deg,#6d6a66 0%,#9b958c 40%,#c9c3b8 70%,#8f8b86 100%);clip-path:polygon(0 0,100% 0,100% 85%,50% 100%,0 86%)}
.hero-title{left:62px;top:300px;font-family:'Poppins',sans-serif;font-weight:600;font-size:60px;line-height:66px;color:#111}
.hero-title span{color:var(--yellow)}
.hero-text{left:62px;top:442px;width:420px;font-size:12.5px;line-height:19px;color:#222}
.btn-yellow{left:60px;top:523px;width:135px;height:37px;background:var(--yellow);color:#222;font-size:13px;font-weight:600;display:flex;align-items:center;justify-content:center;clip-path:polygon(0 0,100% 0,88% 100%,0 100%)}
.badge{width:86px;height:86px;border-radius:50%;background:#fff;box-shadow:0 4px 14px rgba(0,0,0,.18)}
.badge i{position:absolute;left:31px;top:31px;width:24px;height:24px;border-radius:50%;background:var(--yellow)}

/* solution */
.sec-title{font-size:26px}
.num{width:46px;height:46px;background:var(--yellow-soft);clip-path:polygon(50% 0,100% 25%,100% 75%,50% 100%,0 75%,0 25%);display:flex;align-items:center;justify-content:center;font-weight:700;font-size:17px;color:#222}
.num-text{width:410px;font-size:12px;line-height:22px;color:#777}
.diagram{left:735px;top:828px;width:360px;height:314px;background:radial-gradient(circle,#fff3c9 0%,#f7d35c 45%,#8a8a8a 100%);clip-path:polygon(25% 0,75% 0,100% 50%,75% 100%,25% 100%,0 50%)}

/* celebrate */
.band-yellow{left:0;top:1233px;width:757px;height:450px;background:var(--yellow)}
.band-photo-left{left:0;top:1233px;width:255px;height:450px;background:linear-gradient(160deg,#44505e,#b9b3ab);clip-path:polygon(0 0,100% 0,58% 100%,0 100%)}
.band-photo-right{left:757px;top:1233px;width:443px;height:450px;background:linear-gradient(160deg,#6b6864,#b8b1a6 55%,#545b64)}
.celebrate-title{left:295px;top:1330px;font-size:27px;white-space:nowrap;color:#222}
.celebrate-text{width:400px;font-size:12px;line-height:19.5px;color:#fff}
.arrow-dot{width:30px;height:30px;border-radius:50%;background:var(--yellow);display:flex;align-items:center;justify-content:center}
.play{left:866px;top:1447px;width:44px;height:44px;border-radius:50%;background:#fff;border:3px solid rgba(255,255,255,.5);box-shadow:0 0 0 4px rgba(0,0,0,.15);display:flex;align-items:center;justify-content:center}
.watch{left:927px;top:1460px;font-size:13px;color:#fff;font-weight:500}

/* team */
.member-photo{background:linear-gradient(180deg,#d9d4ce,#7d7772)}
.member-name{font-size:15px;font-weight:600;color:#222;text-align:center}
.social{left:540px;width:32px;height:32px;background:var(--yellow);border-radius:3px}
.team-list{left:690px;top:1830px;width:420px;list-style:none;font-size:12px;line-height:19px;color:#777}
.team-list li{position:relative;padding-left:23px;margin-bottom:15px}
.team-list li::before{content:"";position:absolute;left:2px;top:3px;width:7px;height:7px;border-top:3px solid var(--yellow);border-right:3px solid var(--yellow);transform:rotate(45deg)}

/* services */
.services{left:0;top:2090px;width:1200px;height:496px;background:var(--dark);clip-path:polygon(0 0,50% 56px,100% 0,100% 100%,0 100%)}
.services-title{left:0;width:1200px;top:2220px;text-align:center;font-size:32px;color:#fff}
.svc-list{list-style:none;font-size:12px;line-height:22.5px;color:#ddd}
.svc-list li{padding-left:17px;position:relative}
.svc-list li::before{content:"";position:absolute;left:1px;top:8px;width:6px;height:6px;border:1.5px solid var(--yellow);transform:rotate(45deg)}

/* contact */
.hex-photo{left:90px;top:2718px;width:368px;height:410px;background:linear-gradient(135deg,#3e6a92,#a7c2d6 50%,#2d4d6d);clip-path:polygon(50% 0,100% 25%,100% 75%,50% 100%,0 75%,0 25%)}
.hex-inner{left:170px;top:2812px;width:208px;height:230px;background:rgba(255,255,255,.72);clip-path:polygon(50% 0,100% 25%,100% 75%,50% 100%,0 75%,0 25%)}
.years{left:170px;width:208px;top:2900px;text-align:center;font-family:'Rubik',sans-serif;font-weight:500;color:#222;font-size:36px;line-height:36px}
.years small{display:block;font-size:18px;line-height:22px}
.contact-title{left:571px;top:2774px;font-size:30px;line-height:38px}
.field{width:263px;height:38px;background:var(--light);border:1px solid #ddd;font-size:11px;color:#555;padding:0 8px;display:flex;align-items:center}
.btn-gray{left:570px;top:3027px;width:135px;height:36px;background:var(--gray);color:#fff;font-size:13px;font-weight:500;display:flex;align-items:center;justify-content:center;clip-path:polygon(0 0,100% 0,88% 100%,0 100%)}

/* footer */
.footer{left:0;top:3190px;width:1200px;height:340px;background:linear-gradient(120deg,#1e1e1e,#2f2c29 55%,#1f1f1f)}
.foot-brand{left:60px;top:3356px;font-size:22px;font-weight:600;color:var(--yellow);line-height:22px;letter-spacing:1px}
.foot-brand small{display:block;font-size:10px;letter-spacing:3px;color:#888;font-weight:500}
.foot-title{font-family:'Rubik',sans-serif;font-weight:500;font-size:19px;color:var(--yellow)}
.foot-list{list-style:none;font-size:12px;line-height:22.5px;color:#ccc}
.foot-list li{padding-left:24px;position:relative}
.foot-list li::before{content:"";position:absolute;left:2px;top:8px;width:6px;height:6px;border:1.5px solid var(--yellow);transform:rotate(45deg)}
.foot-contact{font-size:12px;line-height:18px;color:#ccc;padding-left:30px}
.copy{left:0;top:3530px;width:1200px;height:36px;background:#555;color:#eee;font-size:11px;display:flex;align-items:center;justify-content:center}
</style>
</head>
<body>

<!-- header -->
<div class="abs brand-mark"></div>
<div class="abs brand">SUMMIT HR<small>CONSULTING</small></div>
<div class="abs header-line"></div>

<svg class="abs info-icon" style="left:380px;top:22px" viewBox="0 0 30 30" fill="none" stroke="#555" stroke-width="1.5"><path d="M15 25s-7-8-7-13a7 7 0 0 1 14 0c0 5-7 13-7 13z"/><circle cx="15" cy="12" r="2.5"/><path d="M5 27h20"/></svg>
<div class="abs info" style="left:438px;top:22px"><b>LOCATION</b>Lorem Ipsum is simply dummy</div>
<svg class="abs info-icon" style="left:692px;top:22px" viewBox="0 0 30 30" fill="none" stroke="#555" stroke-width="1.5"><circle cx="10" cy="8" r="3.5"/><path d="M3 22c0-5 3-8 7-8s7 3 7 8"/><circle cx="22" cy="12" r="3"/><path d="M17 27c1-4 3-6 5-6s4 2 5 6"/></svg>
<div class="abs info" style="left:753px;top:22px"><b>FREE CONSULTAION</b>info@summithrconsulting.com</div>
<div class="abs quote-btn">GET A QUOTE</div>
<div class="abs navbar"></div>
<nav class="abs nav">
  <span class="active">HOME</span><span>RESOURCE SOLUTION</span><span>ABOUT US</span><span>OUR TEAM</span><span>OUR SERVICES</span><span>CONTACT US</span>
</nav>
<svg class="abs" style="left:1069px;top:84px" width="18" height="18" viewBox="0 0 18 18" fill="none" stroke="#fff" stroke-width="2"><circle cx="7" cy="7" r="5"/><path d="M11 11l5 5"/></svg>

<!-- hero -->
<div class="abs hero" role="img" aria-label="Photo of a diverse team shaking hands across an office table"></div>
<h1 class="abs hero-title">HR <span>SUMMIT</span><br>CONSULTING</h1>
<p class="abs hero-text">For fifteen years our team of industry experts has been providing HR consulting services with innovative strategies and a partnership mentality</p>
<div class="abs btn-yellow">LEARN MORE</div>
<div class="abs badge" style="left:557px;top:708px"><i></i></div>

<!-- solution -->
<h2 class="abs sec-title" style="left:110px;top:840px">Your Human Resources Solution</h2>
<div class="abs num" style="left:95px;top:929px">01</div>
<p class="abs num-text" style="left:166px;top:925px">HR Summit Consulting is the solution to all your HR issues. We are a one-stop-shop providing a variety of services</p>
<div class="abs num" style="left:95px;top:997px">02</div>
<p class="abs num-text" style="left:166px;top:993px">Whether you have a specific HR need or seek relief by outsourcing altogether, we have you covered</p>
<div class="abs num" style="left:95px;top:1064px">03</div>
<p class="abs num-text" style="left:166px;top:1060px">For some clients, an HR Summit Consultant is known as the HR department and for others, we simply step in as needed on a project basis</p>
<div class="abs diagram" role="img" aria-label="Illustration of six hexagonal service icons arranged in a flower"></div>

<!-- celebrate -->
<div class="abs band-yellow"></div>
<div class="abs band-photo-left" role="img" aria-label="Photo of smiling colleagues working together at a laptop"></div>
<div class="abs band-photo-right" role="img" aria-label="Photo of a diverse team meeting around a table"></div>
<h2 class="abs celebrate-title">Celebrating 15 Years In Business</h2>
<p class="abs celebrate-text" style="left:275px;top:1392px">For fifteen years our team of industry experts has been providing HR consulting services with innovative strategies and a partnership mentality</p>
<p class="abs celebrate-text" style="left:267px;top:1475px">We have worked with some of the most innovative companies in Silicon Valley, across a broad range of industries, and we're proud to grow our client list every year</p>
<p class="abs celebrate-text" style="left:260px;top:1557px">HR Summit's experienced professionals help implement and maintain best practices, allowing our clients to focus on their core competencies</p>
<div class="abs arrow-dot" style="left:198px;top:1401px"><svg width="10" height="12" viewBox="0 0 10 12"><path d="M2 1l5 5-5 5" stroke="#222" stroke-width="2.5" fill="none"/></svg></div>
<div class="abs arrow-dot" style="left:180px;top:1484px"><svg width="10" height="12" viewBox="0 0 10 12"><path d="M2 1l5 5-5 5" stroke="#222" stroke-width="2.5" fill="none"/></svg></div>
<div class="abs arrow-dot" style="left:157px;top:1566px"><svg width="10" height="12" viewBox="0 0 10 12"><path d="M2 1l5 5-5 5" stroke="#222" stroke-width="2.5" fill="none"/></svg></div>
<div class="abs play"><svg width="12" height="14" viewBox="0 0 12 14"><path d="M2 1l9 6-9 6z" fill="#222"/></svg></div>
<div class="abs watch">WATCH A VIDEO</div>

<!-- team -->
<div class="abs member-photo" style="left:60px;top:1765px;width:208px;height:210px" role="img" aria-label="Portrait of a team member holding a folder"></div>
<svg class="abs" style="left:60px;top:1980px" width="203" height="36" viewBox="0 0 203 36"><path d="M0 0h203v6L101 36 0 26z" fill="#666"/></svg>
<div class="abs member-name" style="left:60px;top:2028px;width:203px">Dana Whitfield</div>
<div class="abs member-photo" style="left:345px;top:1755px;width:185px;height:208px" role="img" aria-label="Portrait of a team member in a blue blouse"></div>
<svg class="abs" style="left:330px;top:1963px" width="203" height="36" viewBox="0 0 203 36"><path d="M0 0h203v8L101 28 0 36z" fill="var(--yellow)"/></svg>
<div class="abs member-name" style="left:330px;top:2006px;width:203px">Dana Whitfield</div>
<div class="abs social" style="top:1866px"></div>
<div class="abs social" style="top:1908px;background:#333"></div>
<h2 class="abs sec-title" style="left:690px;top:1763px;font-size:30px">Our Team</h2>
<ul class="abs team-list">
  <li>Our team is woman-owned, women-led and partnership-oriented</li>
  <li>Working with us means you're hiring senior-level talent that acts as an extension of your company</li>
  <li>We're here to educate companies and help them solve complex HR problems</li>
  <li>Information about our CEO, Dana Whitfield, can be found here</li>
</ul>

<!-- services -->
<div class="abs services"></div>
<h2 class="abs services-title">Services</h2>
<ul class="abs svc-list" style="left:180px;top:2320px">
  <li>Review handbook annually</li><li>Roll out training</li><li>Write offer letters</li><li>Handle employee data and files</li><li>Conduct I-9 audits</li><li>Handle merit and review bonuses</li>
</ul>
<ul class="abs svc-list" style="left:818px;top:2320px">
  <li>Onboarding/Offboarding</li><li>Employee relations</li><li>Investigations</li><li>Leave administration</li><li>Immigration liaison</li><li>Compensation management</li><li>Full cycle recruitment</li>
</ul>
<svg class="abs" style="left:300px;top:2300px" width="610" height="345" viewBox="0 0 610 345">
  <path d="M158 5l134 80v135l-54 32-80-50V5z" fill="var(--yellow)"/>
  <path d="M176 40l98 58v110l-36 20-62-38z" fill="#fff"/>
  <path d="M452 5L318 85v135l54 32 80-50V5z" fill="var(--yellow)"/>
  <path d="M434 40l-98 58v110l36 20 62-38z" fill="#fff"/>
  <path d="M13 253l115-65 115 65-115 85z" fill="#111"/>
  <path d="M366 253l115-65 115 65-115 85z" fill="#111"/>
  <circle cx="216" cy="92" r="13" fill="none" stroke="#333" stroke-width="2"/>
  <circle cx="398" cy="85" r="5" fill="none" stroke="#333" stroke-width="2"/>
  <path d="M385 110h26M390 98h16v12" stroke="#333" stroke-width="2" fill="none"/>
  <circle cx="145" cy="230" r="12" fill="none" stroke="var(--yellow)" stroke-width="2.5" stroke-dasharray="5 3"/>
  <circle cx="466" cy="218" r="7" fill="none" stroke="var(--yellow)" stroke-width="2"/>
  <text x="230" y="132" text-anchor="middle" font-family="Poppins,sans-serif" font-size="14" font-weight="500" fill="#222">Recurring</text>
  <text x="230" y="156" text-anchor="middle" font-family="Poppins,sans-serif" font-size="14" font-weight="500" fill="#222">Procedures</text>
  <text x="381" y="132" text-anchor="middle" font-family="Poppins,sans-serif" font-size="14" font-weight="500" fill="#222">Managing</text>
  <text x="381" y="156" text-anchor="middle" font-family="Poppins,sans-serif" font-size="14" font-weight="500" fill="#222">Functions</text>
  <text x="143" y="275" text-anchor="middle" font-family="Poppins,sans-serif" font-size="15" font-weight="500" fill="#fff">Setup</text>
  <text x="474" y="266" text-anchor="middle" font-family="Poppins,sans-serif" font-size="14" font-weight="500" fill="#fff">Partner</text>
  <text x="474" y="284" text-anchor="middle" font-family="Poppins,sans-serif" font-size="14" font-weight="500" fill="#fff">Communications</text>
</svg>
<div class="abs badge" style="left:563px;top:2520px"><i></i></div>

<!-- contact -->
<div class="abs hex-photo" role="img" aria-label="Photo of a smiling professional woman with glasses"></div>
<div class="abs hex-inner"></div>
<div class="abs years">15 Years<small>Of Provide</small></div>
<h2 class="abs contact-title">Contact&nbsp; Us For a Free<br>Consultation</h2>
<div class="abs field" style="left:570px;top:2862px">For My Business *</div>
<div class="abs field" style="left:844px;top:2862px">Company *</div>
<div class="abs field" style="left:570px;top:2914px">First Name *</div>
<div class="abs field" style="left:844px;top:2914px">Last Name *</div>
<div class="abs field" style="left:570px;top:2966px">Email *</div>
<div class="abs field" style="left:844px;top:2966px">Phone *</div>
<div class="abs btn-gray">GET STARTD</div>

<!-- footer -->
<div class="abs footer" role="img" aria-label="Dim background photo of an office team"></div>
<div class="abs badge" style="left:557px;top:3180px"><i></i></div>
<div class="abs foot-brand">SUMMIT HR<small>CONSULTING</small></div>
<h3 class="abs foot-title" style="left:337px;top:3302px">Site Map</h3>
<ul class="abs foot-list" style="left:337px;top:3337px"><li>Home</li><li>About Us</li><li>Resource Solution</li><li>Our Team</li><li>Our Services</li><li>Contact Us</li></ul>
<h3 class="abs foot-title" style="left:613px;top:3302px">Support</h3>
<ul class="abs foot-list" style="left:613px;top:3337px"><li>Partner</li><li>Careers</li><li>Tearms Of Services</li><li>Privacy Policy</li><li>Client Support</li></ul>
<h3 class="abs foot-title" style="left:889px;top:3302px">Contact Us</h3>
<svg class="abs" style="left:887px;top:3340px" width="22" height="22" viewBox="0 0 22 22" fill="none" stroke="var(--yellow)" stroke-width="1.5"><path d="M11 19s-6-6-6-10a6 6 0 0 1 12 0c0 4-6 10-6 10z"/><circle cx="11" cy="9" r="2"/></svg>
<p class="abs foot-contact" style="left:889px;top:3340px;width:240px">Lorem Ipsum is simply dummy text of the printing and</p>
<svg class="abs" style="left:887px;top:3395px" width="20" height="20" viewBox="0 0 20 20" fill="none" stroke="var(--yellow)" stroke-width="1.5"><path d="M4 2h4l2 5-2.5 1.5a10 10 0 0 0 4 4L13 10l5 2v4a2 2 0 0 1-2 2C8 18 2 12 2 4a2 2 0 0 1 2-2z"/></svg>
<p class="abs foot-contact" style="left:889px;top:3396px">+1 000 000 000</p>
<svg class="abs" style="left:887px;top:3441px" width="20" height="20" viewBox="0 0 20 20" fill="none" stroke="var(--yellow)" stroke-width="1.5"><rect x="2" y="4" width="16" height="12"/><path d="M2 4l8 7 8-7"/></svg>
<p class="abs foot-contact" style="left:889px;top:3442px">info@summithrconsulting.com</p>
<div class="abs copy">© 2021 SUMMIT HR CONSULTING. All rights reserved.</div>

</body>
</html>
```